Private Gym Needs a Rack Card Design

We need a basic front and back rack card (same size as post card) that gives basic information about our brand, and includes our logo. Please see attached logo and required content below.

Target Market(s)

Upscale, private gym.

Industry/Entity Type

Gym

Font styles to use
Sans Serif

Colors
ffffff
5c5c5c
000000
dbdbdb
f78f20

Requirements
Must have
• Business Logo and the following text in a clean, modern, easy-to-read, artistic manner. Style and design must be clean, incorporate our color scheme of MOSTLY white, light grey, charcoal, with just pops of orange. We want the card itself to be mostly white background. Must include website URL as well: corevantagestudio.com
• FRONT CARD:
• Logo
• A safe and individualized approach to exercise
• Our method employs the latest weight resistance training exercises and coaching for healthy living. Not only is our workout methodology effective, it’s safe.
• Our Method…
• -Improves Functional Movement
• -Promotes Weight Loss
• -Builds Strength
• -Increases Flexibility 

• BACK:
• Change Your Body. Find Your Strength.
• There’s 40 years of success behind our proven method
• What is The Formwell? 
• The Formwell is all about teaching our clients how to lift weights and exercise with the proper technique. There’s no slinging or jerking at our gym; only controlled movements that yield real results.
• Come workout with us in our private gym. We are located in Durham adjacent to Harlow Campus and 5 minutes from downtown Durham.
• Address: 482 Linden Ave, Durham, NC 27705
• Phone: (919) 555-2741
• Hours: 9:00 AM – 9:00 PM
Nice to have
• Great organization of text, maybe some columns, colored bullet points, cool graphics and logos.
Should not have
• Busy or crowded design. All lines should be sleek, straight, and streamline. NO STOCK IMAGES, but logos are GREAT

```html
<!DOCTYPE html>
<html lang="en">
<head>
<meta charset="utf-8">
<title>The Formwell – Rack Card Back</title>
<link href="https://fonts.googleapis.com/css2?family=Open+Sans:wght@400;600;700;800&display=swap" rel="stylesheet">
<style>
  :root {
    --page-bg: #d9d9d9;
    --card-bg: #f1f2f4;
    --band: #dfe0e3;
    --charcoal: #5c5c5c;
    --body-grey: #8e9094;
    --watermark: #e3e4e7;
    --orange: #e8723c;
  }
  html, body {
    margin: 0;
    width: 1200px;
    height: 1200px;
    overflow: hidden;
    background: var(--page-bg);
    font-family: "Open Sans", sans-serif;
  }
  .rack-card {
    position: absolute;
    left: 40px;
    top: 202px;
    width: 1120px;
    height: 796px;
    background: var(--card-bg);
    overflow: hidden;
    color: var(--charcoal);
  }
  .side-band {
    position: absolute;
    top: 0;
    width: 60px;
    height: 100%;
    background: var(--band);
  }
  .side-band--left { left: 0; }
  .side-band--right { right: 0; }

  .brand {
    position: absolute;
    top: 56px;
    left: 0;
    width: 100%;
    text-align: center;
    font-weight: 700;
    color: var(--charcoal);
  }
  .brand__the {
    display: block;
    font-size: 20px;
    line-height: 22px;
    letter-spacing: 0.5px;
    margin-left: -250px;
  }
  .brand__name {
    display: block;
    font-size: 56px;
    line-height: 60px;
    letter-spacing: -1.5px;
  }
  .brand__tagline {
    display: block;
    font-size: 15px;
    letter-spacing: 5.2px;
    margin-top: 2px;
  }

  .watermark {
    position: absolute;
    top: 214px;
    left: 0;
    width: 100%;
    text-align: center;
    font-weight: 800;
    font-size: 178px;
    letter-spacing: -4px;
    color: var(--watermark);
    line-height: 1;
    white-space: nowrap;
  }
  .headline {
    position: absolute;
    top: 282px;
    left: 0;
    width: 100%;
    text-align: center;
  }
  .headline__title {
    margin: 0;
    font-size: 33px;
    font-weight: 700;
    letter-spacing: -1.6px;
  }
  .headline__sub {
    margin: 6px 0 0;
    font-size: 17px;
    font-weight: 600;
    color: var(--orange);
  }

  .column {
    position: absolute;
    top: 460px;
  }
  .column--about { left: 158px; width: 420px; }
  .column--visit { left: 655px; width: 340px; }
  .column__title {
    margin: 0;
    font-size: 26px;
    font-weight: 700;
    line-height: 32px;
  }
  .column__lead {
    margin: 2px 0 0;
    font-size: 17px;
    color: var(--charcoal);
  }
  .column__text {
    margin: 22px 0 0;
    font-size: 17px;
    line-height: 28px;
    color: var(--body-grey);
  }
  .column--visit .column__text { margin-top: 20px; }
  .website {
    margin: 26px 0 0;
    font-size: 17px;
    font-weight: 700;
    color: var(--orange);
  }
  .contact-list {
    list-style: none;
    margin: 24px 0 0;
    padding: 0;
  }
  .contact-list li {
    display: flex;
    align-items: center;
    height: 38px;
    font-size: 17px;
    color: var(--body-grey);
  }
  .contact-list svg {
    width: 26px;
    height: 26px;
    margin-right: 18px;
    flex: none;
  }
</style>
</head>
<body>
  <main class="rack-card">
    <div class="side-band side-band--left" role="img" aria-label="Light grey diagonal stripe border"></div>
    <div class="side-band side-band--right" role="img" aria-label="Light grey diagonal stripe border"></div>

    <header class="brand">
      <span class="brand__the">THE</span>
      <span class="brand__name">FORMWELL</span>
      <span class="brand__tagline">PRIVATE TRAINING STUDIO</span>
    </header>

    <div class="watermark" aria-hidden="true">FORMWELL</div>

    <section class="headline">
      <h1 class="headline__title">Change Your Body. Find Your Strength.</h1>
      <p class="headline__sub">There’s 40 years of success behind our proven method</p>
    </section>

    <section class="column column--about">
      <h2 class="column__title">What is The Formwell?</h2>
      <p class="column__text">The Formwell is all about teaching our clients how to lift weights and exercise with the proper technique. There’s no slinging or jerking at our gym; only controlled movements that yield real results.</p>
      <p class="website">www.corevantagestudio.com</p>
    </section>

    <section class="column column--visit">
      <h2 class="column__title">Come workout with us</h2>
      <p class="column__lead">in our private gym.</p>
      <p class="column__text">We are located in Durham adjacent to Harlow Campus and 5 minutes from downtown Durham.</p>
      <ul class="contact-list">
        <li>
          <svg viewBox="0 0 24 24" aria-hidden="true"><path d="M12 2a7 7 0 0 0-7 7c0 5 7 13 7 13s7-8 7-13a7 7 0 0 0-7-7z" fill="var(--orange)"/><circle cx="12" cy="9" r="2.6" fill="var(--card-bg)"/></svg>
          482 Linden Ave, Durham, NC 27705
        </li>
        <li>
          <svg viewBox="0 0 24 24" aria-hidden="true"><path d="M6.6 3.5l2.6 3.3-1.6 2.1a12 12 0 0 0 7.5 7.5l2.1-1.6 3.3 2.6-1.6 2.6c-7.5.4-14.6-6.7-14.2-14.2z" fill="none" stroke="var(--orange)" stroke-width="2" stroke-linejoin="round"/><path d="M14 3a7 7 0 0 1 7 7M14 6.5a3.5 3.5 0 0 1 3.5 3.5" fill="none" stroke="var(--orange)" stroke-width="1.8" stroke-linecap="round"/></svg>
          (919) 555-2741
        </li>
        <li>
          <svg viewBox="0 0 24 24" aria-hidden="true"><circle cx="12" cy="12" r="9.5" fill="none" stroke="var(--orange)" stroke-width="2"/><path d="M12 6.5V12l3.5 3" fill="none" stroke="var(--orange)" stroke-width="2" stroke-linecap="round"/></svg>
          Hours: 9:00 AM – 9:00 PM
        </li>
      </ul>
    </section>
  </main>
</body>
</html>
```